New Business Card Design Project

We want a modern business card that catches the attention of other remodeling companies as well as homeowners. We would like it to be informative but still simple.

Target Market(s)

Residential and other Business's

Contact Information for Business Card

TrellBrix
Phone number is 5153927048
Address is
4817 SW 3rd Lane
Harlow Bend, Ostria 60472
email is trellbrixco@quamlet.com

Requirements
Must have
• Our tagline
• Reliable | Skilled | Fairly Priced

```html
<!DOCTYPE html>
<html lang="en">
<head>
<meta charset="utf-8">
<title>TrellBrix Business Card</title>
<link href="https://fonts.googleapis.com/css2?family=Roboto:wght@400;500;900&display=swap" rel="stylesheet">
<style>
  :root {
    --page: #3a3a3c;
    --card: #2a2a2c;
    --card-panel: #2f2f31;
    --blue: #1b7fe6;
    --orange: #e8620f;
    --white: #f2f2f2;
    --muted: #c9c9cb;
    --divider: #8a8a8c;
  }
  * { box-sizing: border-box; margin: 0; padding: 0; }
  html, body { width: 799px; height: 1200px; overflow: hidden; }
  body {
    background: var(--page);
    font-family: "Roboto", sans-serif;
    position: relative;
  }
  .card {
    position: absolute;
    left: 80px;
    width: 640px;
    height: 366px;
    background: var(--card);
    border-radius: 4px;
    box-shadow: 0 12px 30px rgba(0,0,0,.45);
    overflow: hidden;
  }
  .card--front { top: 150px; }
  .card--back { top: 684px; }

  .brand-name {
    font-family: "Roboto", sans-serif;
    font-weight: 900;
    color: var(--blue);
    text-transform: uppercase;
    letter-spacing: 1px;
    line-height: 1;
  }
  .tagline {
    font-family: "Roboto", sans-serif;
    font-weight: 400;
    color: var(--muted);
    letter-spacing: 0.5px;
    line-height: 1.2;
  }

  /* Front */
  .front-brand {
    position: absolute; left: 0; right: 0; top: 96px;
    text-align: center;
  }
  .front-brand .brand-name { font-size: 78px; }
  .front-brand .tagline { font-size: 20px; margin-top: 14px; }
  .front-web {
    position: absolute; left: 0; right: 0; top: 272px;
    display: flex; align-items: center; justify-content: center; gap: 18px;
    color: var(--white); font-size: 17px;
  }
  .accent-dash { width: 34px; height: 3px; background: var(--orange); }
  .front-web .accent-dash:first-child { transform: translateY(-22px); }
  .front-web .accent-dash:last-child { transform: translateY(22px); }

  /* Back */
  .back-brand {
    position: absolute; left: 24px; top: 140px; width: 270px;
    text-align: center;
  }
  .back-brand .brand-name { font-size: 44px; }
  .back-brand .tagline { font-size: 12.5px; margin-top: 8px; }
  .back-divider {
    position: absolute; left: 306px; top: 60px;
    width: 1px; height: 246px; background: var(--divider);
  }
  .back-panel {
    position: absolute; left: 307px; top: 0; right: 0; bottom: 0;
    background: var(--card-panel);
  }
  .contact {
    position: absolute; left: 336px; top: 70px; right: 20px;
    color: var(--white);
  }
  .contact-name { color: var(--orange); font-weight: 500; font-size: 22px; }
  .contact-role { font-size: 16px; margin-top: 2px; }
  .contact-list { list-style: none; margin-top: 20px; }
  .contact-list li {
    display: flex; align-items: center; gap: 10px;
    font-size: 16px; line-height: 26px;
  }
  .contact-list svg { width: 14px; height: 14px; flex: none; }
  .contact-address { font-size: 16px; line-height: 24px; margin-top: 4px; }
</style>
</head>
<body>
  <section class="card card--front">
    <div class="front-brand">
      <div class="brand-name">TrellBrix</div>
      <div class="tagline">Reliable | Skilled | Fairly Priced</div>
    </div>
    <div class="front-web">
      <span class="accent-dash"></span>
      <span>www.trellbrix.com</span>
      <span class="accent-dash"></span>
    </div>
  </section>

  <section class="card card--back">
    <div class="back-panel"></div>
    <div class="back-brand">
      <div class="brand-name">TrellBrix</div>
      <div class="tagline">Reliable | Skilled | Fairly Priced</div>
    </div>
    <div class="back-divider"></div>
    <div class="contact">
      <div class="contact-name">Jordan Reed Hale</div>
      <div class="contact-role">Managing Director</div>
      <ul class="contact-list">
        <li>
          <svg viewBox="0 0 16 16" aria-hidden="true"><path fill="#e8620f" d="M3.6 1.5 6 4.2 4.7 6c.8 1.8 2.2 3.2 4 4l1.8-1.3 2.7 2.4-1.4 2.4C7 13.5 2.5 9 2 3.2z"/></svg>
          <span>5153927048</span>
        </li>
        <li>
          <svg viewBox="0 0 16 16" aria-hidden="true"><rect x="1" y="3" width="14" height="10" rx="1" fill="#e8620f"/><path d="M1.5 3.5 8 9l6.5-5.5" stroke="#2f2f31" stroke-width="1.4" fill="none"/></svg>
          <span>trellbrixco@quamlet.com</span>
        </li>
        <li>
          <svg viewBox="0 0 16 16" aria-hidden="true"><circle cx="8" cy="8" r="6.5" fill="none" stroke="#e8620f" stroke-width="1.6"/><ellipse cx="8" cy="8" rx="2.8" ry="6.5" fill="none" stroke="#e8620f" stroke-width="1.2"/><path d="M1.5 8h13" stroke="#e8620f" stroke-width="1.2"/></svg>
          <span>www.trellbrix.com</span>
        </li>
      </ul>
      <div class="contact-address">4817 SW 3rd Lane<br>Harlow Bend, Ostria 60472</div>
    </div>
  </section>
</body>
</html>
```